FENRO MIST FOR SPORTS

WE HAVE A LAYOUT FOR A RETAIL BOX.WE NEED TO "MODERNIZE THE LOOK" TO BE MORE CONTEMPORARY AND MORE APPEALING.

Design Front of Box only - Size - 2.625 x 5.375 x 1.5"d

See attached file

```html
<!DOCTYPE html>
<html lang="en">
<head>
<meta charset="UTF-8">
<title>Fenro Mist – No Sweat Wipes – Box Front</title>
<link rel="stylesheet" href="https://fonts.googleapis.com/css2?family=Open+Sans:wght@400;600;700;800&display=swap">
<style>
  :root{
    --page-bg:#ececec;
    --box-white:#ffffff;
    --brand-blue:#3fb6e8;
    --brand-blue-soft:#a9dcf3;
    --mint:#82c99c;
    --text-gray:#8a8a8a;
    --text-dark-gray:#7a7a7a;
    --sky-light:#cfe9f8;
    --sky-mid:#a8d8f3;
    --badge-photo:#9fcfc2;
    --badge-rim:#e9f6fc;
  }
  *{margin:0;padding:0;box-sizing:border-box;}
  html,body{width:1200px;height:927px;overflow:hidden;}
  body{
    background:var(--page-bg);
    font-family:"Open Sans",Arial,sans-serif;
    position:relative;
  }
  .box-front{
    position:absolute;
    left:395px;top:43px;
    width:410px;height:840px;
    background:linear-gradient(to bottom,var(--box-white) 0%,var(--box-white) 52%,var(--sky-light) 72%,var(--sky-mid) 90%);
    overflow:hidden;
    box-shadow:0 2px 10px rgba(0,0,0,.12);
  }
  .new-corner{position:absolute;top:0;right:0;width:110px;height:110px;}
  .brand-banner{position:absolute;left:0;top:78px;width:410px;height:120px;}
  .brand-name{
    position:absolute;left:22px;top:104px;
    font-weight:600;font-size:46px;letter-spacing:1px;
    color:var(--box-white);line-height:1;
  }
  .product-title{
    position:absolute;left:24px;top:226px;
    font-weight:800;font-size:47px;line-height:1.02;
    color:var(--mint);
  }
  .claim{
    position:absolute;left:24px;top:380px;
    font-size:17px;line-height:1.35;color:var(--text-gray);
  }
  .areas{
    position:absolute;left:24px;top:434px;
    font-size:11.5px;color:var(--brand-blue);
  }
  .benefits{
    position:absolute;left:24px;top:470px;
    list-style:none;
    font-weight:700;font-size:15px;line-height:1.65;color:var(--text-dark-gray);
  }
  .benefits li::before{content:". ";}
  .badge{position:absolute;left:208px;top:578px;width:180px;height:180px;z-index:2;}
  .pack-info{
    position:absolute;left:0;bottom:0;width:100%;height:78px;
    background:var(--box-white);
    padding:14px 24px 0;
    color:var(--text-dark-gray);font-weight:700;
    z-index:1;
  }
  .pack-count{font-size:13px;}
  .pack-use{font-size:17px;}
</style>
</head>
<body>
  <main class="box-front">
    <svg class="new-corner" viewBox="0 0 110 110" aria-hidden="true">
      <polygon points="25,0 110,0 110,85" fill="var(--mint)"/>
      <text x="0" y="0" transform="translate(76,32) rotate(45)" text-anchor="middle"
            font-family="Open Sans, sans-serif" font-weight="800" font-size="19" fill="#fff">NEW</text>
    </svg>

    <svg class="brand-banner" viewBox="0 0 410 120" aria-hidden="true">
      <polygon points="0,10 392,10 362,120 0,120" fill="var(--brand-blue-soft)"/>
      <polygon points="0,0 380,0 350,110 0,110" fill="var(--brand-blue)"/>
    </svg>
    <div class="brand-name">FENRO MIST</div>

    <h1 class="product-title">NO<br>SWEAT<br>WIPES</h1>

    <p class="claim">ELIMINATES SWEAT ANYWHERE<br>UP TO 7 DAYS</p>
    <p class="areas">For Scalp, Face, Underarms, Chest, Back, Groin, Legs and Feet</p>

    <ul class="benefits">
      <li>KEEPS SWEAT AWAY FROM EYES</li>
      <li>KEEP A FIRM GRIP</li>
      <li>ELIMINATES ODOR</li>
      <li>WATERPROOF THRU SHOWERING</li>
    </ul>

    <svg class="badge" viewBox="0 0 200 200">
      <defs>
        <path id="badge-arc-top" d="M 26,100 A 74,74 0 0 1 174,100"/>
        <path id="badge-arc-bottom" d="M 14,100 A 86,86 0 0 0 186,100"/>
      </defs>
      <circle cx="100" cy="100" r="98" fill="var(--brand-blue)"/>
      <circle cx="100" cy="100" r="62" fill="var(--badge-rim)"/>
      <circle cx="100" cy="100" r="57" fill="var(--badge-photo)" role="img" aria-label="Photo of a football player leaping in action"/>
      <text font-family="Open Sans, sans-serif" font-weight="800" font-size="15" fill="#fff" letter-spacing="1">
        <textPath href="#badge-arc-top" startOffset="50%" text-anchor="middle">KEEP THE SWEAT OFF</textPath>
      </text>
      <text font-family="Open Sans, sans-serif" font-weight="800" font-size="15" fill="#fff" letter-spacing="1">
        <textPath href="#badge-arc-bottom" startOffset="50%" text-anchor="middle">IMPROVE YOUR GAME</textPath>
      </text>
    </svg>

    <div class="pack-info">
      <p class="pack-count">8 Wipes - 2 Months Supply</p>
      <p class="pack-use">GREAT FOR ALL SPORTS</p>
    </div>
  </main>
</body>
</html>
```